Create/Design Awesome TorvinaRX Label for Pain Cream

I need a label design for a pain relief cream to be sold online in a highly competitve space(brivo). Therefore the label needs to be a killer and really jump off the page.
I am a RN so I want it to have a bit of a clinical look while still embracing an all natural product (blend east & west medicine?). It will be on a small solid white tub (3oz). The look should communicate pain alleviation/relief, all natural feel good, cooling soothing. The product color is like azure/light blue so may could incorporate that.

You can view the competition here: https://www.brivo-shop.example/s/ref=nb_sb_ss_i_2_5?url=search-alias%3Daps&field-keywords=pain+relief+cream&sprefix=pain+%2Caps%2C163

You can see some of my other products here: http://www.brivo-shop.example/s?marketplaceID=QLMRTZPWY4HUS&me=KOB8J2D3XRUMP&merchant=KOB8J2D3XRUMP&redirect=true

TorvinaRX All Natural
Pain Relief
Inflammation
Formulation

with Arnica, B6 & MSM

This should be wording on front of label. May rearrange or add to? Can use template boxes on sides.

Template & Product highlights attached

PS: Hoping on creative & patient designer who can help me make this really awesome. Looking for long term relationship as I have many other products in the works.

Think clinical/professional but still friendly. Like something your doctor od pharmacist may give you. Added Sunday, December 6, 2015

Reason: I was just now able to complete brief with more information. Want to give ample time for best designs.

Target Market(s)

35-90 years old, male and females

Industry/Entity Type

Medical

Colors
85acd3
3377b5
fbee3f
fbed22
ec1f27
ffffff
9bcb3c

Requirements
Must have
• Bright, colorful, clinical all natural look.
Nice to have
• maybe some images of musculo-sketekal (spine, Knees, elbows) in background?
Should not have
• Please do not copy front wording of template

```html
<!DOCTYPE html>
<html lang="en">
<head>
<meta charset="utf-8">
<title>TorvinaRx Natural Pain Relief – Jar Label</title>
<link rel="stylesheet" href="https://fonts.googleapis.com/css2?family=Open+Sans:ital,wght@0,400;0,700;0,800;1,400;1,800&display=swap">
<style>
  :root {
    --navy: #1d2a78;
    --blue-deep: #2456a0;
    --blue-mid: #3377b5;
    --blue-light: #85acd3;
    --white: #ffffff;
    --ink: #1b1b1b;
    --rule: #2b2b2b;
    --stage: #eef0f3;
    --swoosh: #9aa0a8;
  }
  * { box-sizing: border-box; margin: 0; padding: 0; }
  html, body { width: 1200px; height: 1000px; overflow: hidden; }
  body {
    background: var(--stage);
    font-family: "Open Sans", Arial, sans-serif;
    position: relative;
  }
  .label {
    position: absolute;
    left: 40px; top: 250px;
    width: 1120px; height: 500px;
    display: flex;
    background: var(--white);
    box-shadow: 0 4px 18px rgba(0,0,0,.12);
  }

  /* Side facts panels */
  .facts-panel {
    width: 300px; height: 100%;
    padding: 22px 20px;
    color: var(--ink);
    font-size: 9.5px;
    line-height: 1.35;
    position: relative;
  }
  .facts-panel::before {
    content: ""; position: absolute; top: 0; bottom: 0; width: 10px;
    background: linear-gradient(var(--blue-mid), var(--blue-deep));
  }
  .facts-left::before { left: 0; }
  .facts-right::before { right: 0; }
  .facts-box {
    border: 1.5px solid var(--rule);
    padding: 6px 8px;
    height: 100%;
  }
  .facts-title { font-size: 15px; font-weight: 800; border-bottom: 3px solid var(--rule); padding-bottom: 2px; margin-bottom: 4px; }
  .facts-row { border-bottom: 1px solid var(--rule); padding: 3px 0; }
  .facts-row:last-child { border-bottom: none; }
  .facts-head { display: flex; justify-content: space-between; font-weight: 700; }
  .facts-row b { font-weight: 700; }
  .distributor { font-size: 8px; margin-top: 6px; }

  /* Front panel */
  .front {
    width: 520px; height: 100%;
    position: relative;
    overflow: hidden;
  }
  .front-art { position: absolute; inset: 0; }
  .maker {
    position: absolute; left: 55px; top: 62px;
    color: var(--white); font-size: 17px; letter-spacing: .5px;
  }
  .brand-name {
    position: absolute; left: 0; right: 0; top: 150px;
    text-align: center;
    font-weight: 700; font-size: 66px; color: var(--navy);
    letter-spacing: -1px; line-height: 1;
  }
  .claim {
    position: absolute; right: 58px; top: 240px;
    font-weight: 800; font-style: italic; font-size: 25px;
    color: var(--navy); letter-spacing: .5px;
  }
  .subclaim {
    position: absolute; right: 62px; top: 276px;
    font-style: italic; font-size: 18px; color: var(--navy);
  }
  .ingredients {
    position: absolute; left: 0; right: 0; top: 382px; text-align: center;
    font-style: italic; font-size: 36px; color: var(--white);
  }
  .net-weight {
    position: absolute; left: 0; right: 0; top: 448px; text-align: center;
    font-size: 19px; color: var(--white);
  }
</style>
</head>
<body>
  <main class="label">
    <section class="facts-panel facts-left">
      <div class="facts-box">
        <div class="facts-title">Drug Facts</div>
        <div class="facts-row">
          <div class="facts-head"><span>Active ingredient</span><span>Purpose</span></div>
          <div class="facts-head" style="font-weight:400"><span>Arnica Montana 1X</span><span>Topical Analgesic</span></div>
        </div>
        <div class="facts-row"><b>Uses</b> temporarily relieves minor aches and pains of sore muscles and joints associated with arthritis, simple backache, strains, bruises and sprains.</div>
        <div class="facts-row"><b>Warnings</b> For external use only.</div>
        <div class="facts-row"><b>When using this product</b> • avoid contact with eyes or mucous membranes • do not apply to wounds or damaged skin • do not bandage tightly • wash hands after use with cool water</div>
        <div class="facts-row"><b>Stop use and ask a doctor if</b> condition worsens, or symptoms persist for more than 7 days.</div>
        <div class="distributor">Distributed by Orvelle3, 100 Sample Way, Springfield</div>
      </div>
    </section>

    <section class="front">
      <svg class="front-art" width="520" height="500" viewBox="0 0 520 500" aria-hidden="true">
        <defs>
          <linearGradient id="bandBlue" x1="0" y1="0" x2="1" y2="1">
            <stop offset="0" stop-color="#1f4f97"/>
            <stop offset=".5" stop-color="#3377b5"/>
            <stop offset="1" stop-color="#23549e"/>
          </linearGradient>
        </defs>
        <rect width="520" height="500" fill="url(#bandBlue)"/>
        <path d="M0,150 C170,100 360,140 520,100 L520,355 C380,330 200,300 0,280 Z" fill="#ffffff"/>
        <path d="M0,280 C200,300 380,330 520,355" fill="none" stroke="#9aa0a8" stroke-width="6"/>
        <path d="M0,150 C170,100 360,140 520,100" fill="none" stroke="#c9ced6" stroke-width="3"/>
      </svg>
      <div class="maker">ORVELLE3</div>
      <div class="brand-name">TorvinaRx</div>
      <div class="claim">NATURAL PAIN RELIEF</div>
      <div class="subclaim">Topical Analgesic</div>
      <div class="ingredients">With Arnica, B6 &amp; Msm</div>
      <div class="net-weight">Net Wt. 3 oz. (85g)</div>
    </section>

    <section class="facts-panel facts-right">
      <div class="facts-box">
        <div class="facts-title">Drug Facts (continued)</div>
        <div class="facts-row">If pregnant or breast-feeding, ask a health professional before use. <b>Keep out of reach of children.</b> If swallowed, get medical help right away.</div>
        <div class="facts-row"><b>Directions</b> • adults and children 12 years and older: apply to affected area up to 3 to 4 times daily • children under 12: ask a doctor</div>
        <div class="facts-row"><b>Other information</b> store at room temperature</div>
        <div class="facts-row"><b>Inactive ingredients</b> aloe vera leaf juice, MSM, pyridoxine HCl (vitamin B6), menthol, glycerin, emulsifying wax, tocopherol</div>
      </div>
    </section>
  </main>
</body>
</html>
```